Design an Elegant Handbag Brand website

I need a webiste design are looking for ideas for a new theme, color scheme, etc. You come up with the general look and feel of the home page and our team will take it from there.
We're only looking for a one (1) page layout which should be fashionable and graphic intensive, but also include the standard homepage links (about us, see our collections, etc)

Target Market(s)

Our customers are fashionable women looking for an animal friendly and environmentally friendly handbag.

Industry/Entity Type

Business

Number of Pages Required

1 page

Font styles to use
Serif
Sans Serif

Requirements
Must have
• Feel free to modify it with different colors or tweaks as you see fit. We are open to all suggestions.
Nice to have

```html
<!DOCTYPE html>
<html lang="en">
<head>
<meta charset="utf-8">
<title>Handbag Boutique</title>
<link href="https://fonts.googleapis.com/css2?family=Montserrat:wght@400;500;600;700&family=Open+Sans:wght@400;600&display=swap" rel="stylesheet">
<style>
:root{
  --ink:#1d1d1d;
  --muted:#6f6f6f;
  --gray:#8e8e8e;
  --gray-dark:#7c7c7c;
  --gray-light:#efefef;
  --line:#dcdcdc;
  --accent:#b89878;
  --white:#ffffff;
  --star:#a88b6c;
  --bottom:#e4e4e4;
}
*{box-sizing:border-box;margin:0;padding:0}
html,body{width:1200px;height:2824px;overflow:hidden}
body{position:relative;background:var(--white);color:var(--ink);font-family:"Open Sans",Arial,sans-serif;font-size:13px}
section,header,footer,.block{position:absolute;left:0;width:1200px}
h1,h2,h3,h4{font-family:"Montserrat",Arial,sans-serif}
a{color:inherit;text-decoration:none}

.promo-bar{top:0;height:28px;background:#111;color:#fff;font-size:11px;display:flex;align-items:center;justify-content:center}
.promo-bar b{margin:0 4px}

.site-nav{top:28px;height:72px;display:flex;align-items:center;padding:0 140px 0 136px;font-family:"Montserrat",sans-serif;font-size:13px}
.site-nav .menu{display:flex;gap:44px}
.site-nav .menu span::after{content:"";display:inline-block;margin-left:6px;border:4px solid transparent;border-top-color:var(--ink);transform:translateY(2px)}
.site-nav .menu .plain::after{display:none}
.site-nav .tools{margin-left:auto;display:flex;align-items:center;gap:18px}
.search{width:150px;height:26px;border-bottom:1px solid var(--line);display:flex;justify-content:flex-end;align-items:center}
.icon-circle{width:26px;height:26px;border:1px solid var(--ink);border-radius:50%;display:flex;align-items:center;justify-content:center}

.hero{top:100px;height:380px}
.hero-panel{position:absolute;left:0;top:0;width:688px;height:380px;background:var(--gray);padding:38px 0 0 140px;color:#fff}
.hero-panel h1{font-size:42px;line-height:1.1;font-weight:700;width:420px}
.hero-panel p{margin-top:14px;font-size:11px;line-height:1.5;width:300px;opacity:.9}
.btn-white{display:inline-flex;align-items:center;gap:14px;background:#fff;color:var(--ink);font-family:"Montserrat",sans-serif;font-size:12px;font-weight:600;height:38px;padding:0 22px}
.hero-panel .btn-white{position:absolute;left:140px;top:256px}
.hero-photo{position:absolute;left:688px;top:0;width:392px;height:380px;background:radial-gradient(circle at 50% 55%,#c9a780 0,#e6dccf 45%,#f3f1ee 80%)}
.pager{position:absolute;display:flex;gap:6px}
.pager i{width:24px;height:24px;background:var(--accent);display:flex;align-items:center;justify-content:center}
.hero .pager{left:980px;top:300px}

.title-line{display:flex;align-items:center;gap:10px;font-size:22px;font-weight:600}
.title-line::after{content:"";width:160px;height:1px;background:var(--line)}
.title-line .dot{order:2;margin-right:-10px}
.dot{width:9px;height:9px;border-radius:50%;background:var(--accent)}

.about{top:480px;height:360px}
.about-text{position:absolute;left:140px;top:88px;width:360px}
.about-text p{margin-top:26px;font-size:11px;line-height:1.6;color:var(--muted)}
.link-arrow{display:inline-flex;align-items:center;gap:14px;margin-top:26px;font-size:12px;font-family:"Montserrat",sans-serif}
.about-photo{position:absolute;left:688px;top:0;width:512px;height:360px;background:radial-gradient(ellipse at 52% 48%,#6e1420 0,#8b2a33 28%,#e9e3e0 62%,#fff 85%)}

.categories{top:848px;height:412px}
.category{position:absolute;top:0;height:412px;color:#fff;padding:62px 0 0 24px}
.category .label{font-size:12px;letter-spacing:3px}
.category h3{margin-top:22px;font-size:26px;font-weight:500}
.category .link-arrow{position:absolute;bottom:32px;margin:0}
.cat-1{left:0;width:688px;background:linear-gradient(90deg,var(--gray-dark) 0,#8a8680 55%,var(--gray-dark) 100%);padding-left:144px}
.cat-1 .link-arrow{left:144px}
.cat-2{left:692px;width:252px;background:linear-gradient(180deg,#8a8a8a,#9a948e)}
.cat-3{left:948px;width:252px;background:linear-gradient(180deg,#858585,#8f8b86)}
.cat-2 .link-arrow,.cat-3 .link-arrow{left:24px}
.categories-pager{left:948px!important;top:1278px}

.latest-head{top:1352px;left:180px;width:auto}
.products{top:1432px;height:400px;display:flex;gap:4px}
.product{width:297px}
.product-photo{position:relative;height:228px;background:radial-gradient(circle at 50% 55%,var(--pc) 0,#e3e1de 38%,var(--gray-light) 70%)}
.tag{position:absolute;left:8px;top:8px;background:var(--accent);color:#fff;font-size:10px;padding:4px 10px}
.fav{position:absolute;right:10px;top:10px;width:26px;height:26px;border-radius:50%;background:#fff;display:flex;align-items:center;justify-content:center}
.product-info{padding:20px 0 0 8px}
.product-info h4{font-size:13px;font-weight:500}
.price{margin-top:6px;font-size:13px}
.price s{color:var(--muted);margin-right:6px}
.stars{margin-top:8px;display:flex;gap:4px}
.product .link-arrow{margin-top:16px}
.slide-arrow{position:absolute;top:1548px;width:26px;height:26px;border-radius:50%;background:#fff;display:flex;align-items:center;justify-content:center;box-shadow:0 1px 4px rgba(0,0,0,.15)}

.partners-head{top:1912px;left:180px;width:auto}
.partners{top:1990px;height:80px;display:flex;justify-content:center;gap:56px;align-items:center}
.badge{background:#cfcfcf}

.newsletter{top:2120px;height:272px;background:var(--gray);color:#fff;padding:52px 0 0 180px}
.newsletter h2{font-size:42px;font-weight:700}
.newsletter p{margin-top:12px;width:380px;font-size:11px;line-height:1.5;opacity:.9}
.subscribe{position:absolute;left:620px;top:124px;display:flex;gap:10px}
.subscribe .field{width:190px;height:40px;border:1px solid #fff;padding:0 12px;display:flex;align-items:center;font-size:12px}
.subscribe .btn-white{height:40px;width:200px;justify-content:space-between}

.site-footer{top:2420px;height:340px;padding:36px 0 0 180px;display:flex}
.site-footer h4{font-size:16px;font-weight:600;margin-bottom:18px}
.site-footer ul{list-style:none;font-size:11px;line-height:17px;color:var(--ink)}
.col-a{width:240px}.col-b{width:170px}.col-c{width:200px}.col-d{width:240px}
.col-d p{font-size:11px;line-height:1.5;color:var(--ink)}
.cards{margin-top:14px;display:flex;gap:6px}
.cards i{width:42px;height:26px;border:1px solid var(--line);background:#f5f5f5}

.bottom-bar{top:2760px;height:64px;background:var(--bottom);display:flex;align-items:center;padding:0 180px;font-size:11px}
.social{margin-left:auto;display:flex;gap:16px}
.social i{width:10px;height:10px;border-radius:50%;background:#666}
</style>
</head>
<body>

<div class="promo-bar block">Get <b>30% Discount</b> on your first purchase</div>

<header class="site-nav">
  <nav class="menu"><span>Shop</span><span class="plain">Abouts</span><span>Sells</span><span class="plain">Contact</span></nav>
  <div class="tools">
    <div class="search"><svg width="12" height="12" viewBox="0 0 12 12"><circle cx="5" cy="5" r="4" fill="none" stroke="#1d1d1d" stroke-width="1.3"/><path d="M8 8l3 3" stroke="#1d1d1d" stroke-width="1.3"/></svg></div>
    <div class="icon-circle"><svg width="12" height="12" viewBox="0 0 12 12"><circle cx="6" cy="4" r="2.4" fill="none" stroke="#1d1d1d"/><path d="M1.5 11.5c0-3 9-3 9 0" fill="none" stroke="#1d1d1d"/></svg></div>
    <span>View Cart</span>
    <div class="icon-circle"><svg width="12" height="12" viewBox="0 0 12 12"><rect x="2" y="4" width="8" height="7" fill="none" stroke="#1d1d1d"/><path d="M4 4V3a2 2 0 014 0v1" fill="none" stroke="#1d1d1d"/></svg></div>
  </div>
</header>

<section class="hero">
  <div class="hero-panel">
    <h1>Sed ut perspiciatis unde omnis</h1>
    <p>Lorem ipsum dolor sit amet, consectetur adipiscing elit sed do eiusmod tempor incididunt ut labore.</p>
    <a class="btn-white">Shop Now <svg width="22" height="8" viewBox="0 0 22 8"><path d="M0 4h20M17 1l3 3-3 3" fill="none" stroke="#1d1d1d"/></svg></a>
  </div>
  <div class="hero-photo" role="img" aria-label="Three beige leather handbags of different sizes"></div>
  <div class="pager"><i><svg width="8" height="8" viewBox="0 0 8 8"><path d="M5 1L2 4l3 3" fill="none" stroke="#fff"/></svg></i><i><svg width="8" height="8" viewBox="0 0 8 8"><path d="M3 1l3 3-3 3" fill="none" stroke="#fff"/></svg></i></div>
</section>

<section class="about">
  <div class="about-text">
    <h2 class="title-line">About Us <span class="dot"></span></h2>
    <p>Sed ut perspiciatis unde omnis iste natus error sit voluptatem accusantium doloremque laudantium, totam rem aperiam, eaque ipsa quae ab illo inventore veritatis et quasi architecto beatae vitae dicta sunt explicabo. Nemo enim ipsam voluptatem quia voluptas sit aspernatur aut odit aut fugit, sed quia consequuntur.</p>
    <a class="link-arrow">Read More <svg width="22" height="8" viewBox="0 0 22 8"><path d="M0 4h20M17 1l3 3-3 3" fill="none" stroke="#1d1d1d"/></svg></a>
  </div>
  <div class="about-photo" role="img" aria-label="Burgundy croc-textured handbag with gold clasp"></div>
</section>

<section class="categories">
  <div class="category cat-1" role="img" aria-label="Woman in denim walking with a tote bag">
    <div class="label">Category 1</div><h3>Neque porro quisquam</h3>
    <a class="link-arrow">Shop Now <svg width="22" height="8" viewBox="0 0 22 8"><path d="M0 4h20M17 1l3 3-3 3" fill="none" stroke="#fff"/></svg></a>
  </div>
  <div class="category cat-2" role="img" aria-label="Woman in grey coat carrying a handbag">
    <div class="label">Category 2</div><h3>Voluptatem</h3>
    <a class="link-arrow">Shop Now <svg width="22" height="8" viewBox="0 0 22 8"><path d="M0 4h20M17 1l3 3-3 3" fill="none" stroke="#fff"/></svg></a>
  </div>
  <div class="category cat-3" role="img" aria-label="Woman in long coat with a shoulder bag">
    <div class="label">Category 3</div><h3>Consequuntur</h3>
    <a class="link-arrow">Shop Now <svg width="22" height="8" viewBox="0 0 22 8"><path d="M0 4h20M17 1l3 3-3 3" fill="none" stroke="#fff"/></svg></a>
  </div>
</section>
<div class="pager categories-pager"><i><svg width="8" height="8" viewBox="0 0 8 8"><path d="M5 1L2 4l3 3" fill="none" stroke="#fff"/></svg></i><i><svg width="8" height="8" viewBox="0 0 8 8"><path d="M3 1l3 3-3 3" fill="none" stroke="#fff"/></svg></i></div>

<h2 class="title-line block latest-head">Latest Designs <span class="dot"></span></h2>

<section class="products">
  <article class="product">
    <div class="product-photo" style="--pc:#2a2a2a" role="img" aria-label="Black leather tote"><span class="tag">On Sale</span><span class="fav"><svg width="12" height="11" viewBox="0 0 12 11"><path d="M6 10L1.5 5.5A2.5 2.5 0 016 2a2.5 2.5 0 014.5 3.5z" fill="none" stroke="#1d1d1d"/></svg></span></div>
    <div class="product-info"><h4>Duis aute irure</h4><div class="price"><s>$ 400.00</s>$ 300.00</div>
      <div class="stars"><svg width="58" height="10" viewBox="0 0 58 10" fill="#a88b6c"><circle cx="5" cy="5" r="4"/><circle cx="29" cy="5" r="4"/><circle cx="53" cy="5" r="4"/></svg></div>
      <a class="link-arrow">Add to Cart <svg width="22" height="8" viewBox="0 0 22 8"><path d="M0 4h20M17 1l3 3-3 3" fill="none" stroke="#1d1d1d"/></svg></a></div>
  </article>
  <article class="product">
    <div class="product-photo" style="--pc:#5a3a26" role="img" aria-label="Brown leather handbag"><span class="fav"><svg width="12" height="11" viewBox="0 0 12 11"><path d="M6 10L1.5 5.5A2.5 2.5 0 016 2a2.5 2.5 0 014.5 3.5z" fill="none" stroke="#1d1d1d"/></svg></span></div>
    <div class="product-info"><h4>Duis aute irure</h4><div class="price">$ 300.00</div>
      <div class="stars"><svg width="58" height="10" viewBox="0 0 58 10" fill="#a88b6c"><circle cx="5" cy="5" r="4"/><circle cx="29" cy="5" r="4"/><circle cx="53" cy="5" r="4"/></svg></div>
      <a class="link-arrow">Add to Cart <svg width="22" height="8" viewBox="0 0 22 8"><path d="M0 4h20M17 1l3 3-3 3" fill="none" stroke="#1d1d1d"/></svg></a></div>
  </article>
  <article class="product">
    <div class="product-photo" style="--pc:#e0301e" role="img" aria-label="Red structured handbag"><span class="tag">On Sale</span><span class="fav"><svg width="12" height="11" viewBox="0 0 12 11"><path d="M6 10L1.5 5.5A2.5 2.5 0 016 2a2.5 2.5 0 014.5 3.5z" fill="none" stroke="#1d1d1d"/></svg></span></div>
    <div class="product-info"><h4>Duis aute irure</h4><div class="price"><s>$ 600.00</s>$ 400.00</div>
      <div class="stars"><svg width="58" height="10" viewBox="0 0 58 10" fill="#a88b6c"><circle cx="5" cy="5" r="4"/><circle cx="29" cy="5" r="4"/><circle cx="53" cy="5" r="4"/></svg></div>
      <a class="link-arrow">Add to Cart <svg width="22" height="8" viewBox="0 0 22 8"><path d="M0 4h20M17 1l3 3-3 3" fill="none" stroke="#1d1d1d"/></svg></a></div>
  </article>
  <article class="product">
    <div class="product-photo" style="--pc:#c9a780" role="img" aria-label="Set of beige handbags"><span class="fav"><svg width="12" height="11" viewBox="0 0 12 11"><path d="M6 10L1.5 5.5A2.5 2.5 0 016 2a2.5 2.5 0 014.5 3.5z" fill="none" stroke="#1d1d1d"/></svg></span></div>
    <div class="product-info"><h4>Duis aute irure</h4><div class="price">$ 180.00</div>
      <div class="stars"><svg width="58" height="10" viewBox="0 0 58 10" fill="#a88b6c"><circle cx="5" cy="5" r="4"/><circle cx="29" cy="5" r="4"/><circle cx="53" cy="5" r="4"/></svg></div>
      <a class="link-arrow">Add to Cart <svg width="22" height="8" viewBox="0 0 22 8"><path d="M0 4h20M17 1l3 3-3 3" fill="none" stroke="#1d1d1d"/></svg></a></div>
  </article>
</section>
<span class="slide-arrow" style="left:8px"><svg width="8" height="8" viewBox="0 0 8 8"><path d="M5 1L2 4l3 3" fill="none" stroke="#1d1d1d"/></svg></span>
<span class="slide-arrow" style="left:1166px"><svg width="8" height="8" viewBox="0 0 8 8"><path d="M3 1l3 3-3 3" fill="none" stroke="#1d1d1d"/></svg></span>

<h2 class="title-line block partners-head">Our Partners <span class="dot"></span></h2>
<section class="partners">
  <span class="badge" style="width:56px;height:56px;border-radius:50%"></span>
  <span class="badge" style="width:96px;height:40px"></span>
  <span class="badge" style="width:64px;height:56px;border-radius:50%"></span>
  <span class="badge" style="width:80px;height:40px"></span>
  <span class="badge" style="width:96px;height:40px"></span>
  <span class="badge" style="width:88px;height:56px"></span>
</section>

<section class="newsletter">
  <h2>vitae dicta sunt</h2>
  <p>Lorem ipsum dolor sit amet, consectetur adipiscing elit, sed do eiusmod tempor incididunt ut labore et dolore magna aliqua. Ut enim ad minim veniam, quis nostrud exercitation ullamco laboris nisi ut aliquip ex ea commodo consequat.</p>
  <div class="subscribe"><div class="field">Email</div><a class="btn-white">Subscribe <svg width="22" height="8" viewBox="0 0 22 8"><path d="M0 4h20M17 1l3 3-3 3" fill="none" stroke="#1d1d1d"/></svg></a></div>
</section>

<footer class="site-footer">
  <div class="col-a"><h4>Our Collections</h4><ul><li>Duis aute</li><li>Irure dolor</li><li>Ullam labore</li><li>Ex fugiat</li><li>Esse proident</li><li>Excepteur sint</li><li>Occaecat</li><li>Cupidatat non proident</li></ul></div>
  <div class="col-b"><h4>Gifts</h4><ul><li>Nulla pariatur</li><li>Sit amet</li><li>Illo inventore</li><li>Veritatis et quasi</li><li>Architecto beatae</li></ul></div>
  <div class="col-c"><h4>Useful Links</h4><ul><li>About</li><li>Privacy Policy</li><li>Shop</li><li>Contact</li><li>Terms &amp; Conditions</li></ul></div>
  <div class="col-d"><h4>Contact Info</h4><p>Lorem ipsum dolor sit amet, consectetur adipiscing elit sed do eiusmod tempor incididunt ut labore.</p><div class="cards"><i></i><i></i><i></i><i></i></div></div>
</footer>

<div class="bottom-bar block">All Rights Reserved<div class="social"><i></i><i></i><i></i></div></div>

</body>
</html>
```